BrightFold Partners Advisory needs business cards

BrightFold Partners Advisory is a new approach to consulting: we believe in partnering our clients in a hands-on, side-by-side, rolling-up-our sleeves approach, rather than being removed and aloof consultants.

We have a logo design developped through PixelHarbor (see attachment) and need to move to the stage of designing a business card for our 7 founding members.

Target Market(s)

Senior executives in local and global companies (such as Fizzmont Soda, Parvanta, Dorvik, etc)

Industry/Entity Type

Business

Requirements
Must have
• Look and feel: The design reflect the logo: i.e. professional, modern and approachable (as opposed to corporate traditional and remote). We are looking for a high quality, premium design.

Content must haves:
- prominent: our logo, person's name, function, phone number and e-mail address
- less prominent: company address and website

Example: BrightFold Partners Advisory logo, Maren Vollers, Partner, +44 (0)782 307 5918, maren_vollers@brightfoldpartners.example / 17 Harrowgate Lane, Esher, Surrey, UK, KT10 3PW - www.brightfoldpartners.example

- Both sides of the card can be used
- Both versions of the logo can be used (on black or on white)

```html
<!DOCTYPE html>
<html lang="en">
<head>
<meta charset="utf-8">
<title>BrightFold Partners Advisory – Business Cards</title>
<link href="https://fonts.googleapis.com/css2?family=Arimo:wght@400;700&display=swap" rel="stylesheet">
<style>
  :root {
    --backdrop: #4a2e1a;
    --card-top: #ffffff;
    --card-bottom: #e4e4e4;
    --ink: #222222;
    --ink-soft: #555555;
    --brand-blue: #2a8fcc;
    --brand-blue-light: #5cc0ee;
    --band-blue: #3399cc;
    --ghost-blue: rgba(150, 195, 215, 0.35);
  }
  * { margin: 0; padding: 0; box-sizing: border-box; }
  html, body {
    width: 1157px;
    height: 1200px;
    overflow: hidden;
    background: var(--backdrop);
    font-family: "Arimo", Arial, sans-serif;
  }
  .card {
    position: absolute;
    left: 239px;
    width: 689px;
    height: 403px;
    background: linear-gradient(to bottom, var(--card-top), var(--card-bottom));
    overflow: hidden;
  }
  .card--front { top: 145px; }
  .card--back { top: 622px; }

  .brand-dot {
    position: absolute;
    border-radius: 50%;
    background: radial-gradient(circle at 35% 35%, var(--brand-blue-light), var(--brand-blue));
  }
  .brand-name {
    position: absolute;
    color: var(--ink);
    font-weight: 400;
    line-height: 1;
    white-space: nowrap;
  }
  .card--front .brand-dot { left: 115px; top: 97px; width: 166px; height: 166px; }
  .card--front .brand-name { left: 300px; top: 140px; }
  .card--front .brand-name__main { display: block; font-size: 58px; letter-spacing: -1px; }
  .card--front .brand-name__sub { display: block; font-size: 21px; letter-spacing: 0.5px; margin-top: 6px; }

  .card--back .brand-dot { left: 40px; top: 55px; width: 84px; height: 84px; }
  .card--back .brand-name { left: 134px; top: 82px; }
  .card--back .brand-name__main { display: block; font-size: 28px; letter-spacing: -0.5px; }
  .card--back .brand-name__sub { display: block; font-size: 10px; letter-spacing: 0.3px; margin-top: 3px; }

  .divider {
    position: absolute;
    left: 282px;
    top: 36px;
    width: 2px;
    height: 130px;
    background: var(--ink-soft);
  }
  .contact {
    position: absolute;
    left: 305px;
    top: 48px;
    font-size: 17px;
    line-height: 1.35;
    color: var(--ink);
  }
  .contact__role { color: var(--brand-blue); }
  .contact__details { margin-top: 18px; color: var(--ink-soft); font-size: 16px; }

  .ghost-mark { position: absolute; left: 0; top: 0; }
  .accent-band {
    position: absolute;
    left: 0;
    bottom: 0;
    width: 100%;
    height: 10px;
    background: var(--band-blue);
  }
</style>
</head>
<body>
  <section class="card card--front" aria-label="Card front">
    <div class="brand-dot"></div>
    <div class="brand-name">
      <span class="brand-name__main">BrightFold</span>
      <span class="brand-name__sub">PARTNERS ADVISORY</span>
    </div>
  </section>

  <section class="card card--back" aria-label="Card back">
    <svg class="ghost-mark" width="689" height="403" aria-hidden="true">
      <circle cx="506" cy="390" r="188" fill="var(--ghost-blue)"/>
    </svg>
    <div class="brand-dot"></div>
    <div class="brand-name">
      <span class="brand-name__main">BrightFold</span>
      <span class="brand-name__sub">PARTNERS ADVISORY</span>
    </div>
    <div class="divider"></div>
    <div class="contact">
      <div class="contact__name">Maren Vollers</div>
      <div class="contact__role">Partner</div>
      <div class="contact__details">
        <div>+44 (0)782 307 5918</div>
        <div>maren_vollers@brightfoldpartners.example</div>
      </div>
    </div>
    <div class="accent-band"></div>
  </section>
</body>
</html>
```